Local Real Estate Office needs an innovative Letterhead Design

Using the attached Logo, please create a letterhead design that is innovative and unusual. I am looking for something that will appeal to young homebuyers as well as seniors going into Condos.

The attached logo for Marrowfield Hearth needs to be included (small but readable) as well as spaces for 2 agents "head shots" photos.
Updates

I need a spot on the letterhead for two photos (head shots). thx

Industry/Entity Type

Real Estate

```html
<!DOCTYPE html>
<html lang="en">
<head>
<meta charset="utf-8">
<title>Prairieview Real Estate Letterhead</title>
<link href="https://fonts.googleapis.com/css2?family=Open+Sans:wght@400;600;700;800&display=swap" rel="stylesheet">
<style>
  :root {
    --backdrop: #8f8f8f;
    --paper: #ffffff;
    --navy: #0d2c5e;
    --navy-deep: #08224c;
    --badge: #123a7a;
    --ink: #3a3a3a;
    --muted: #8a8a8a;
    --photo-frame: #dfe3ea;
    --photo-senior: #b9b3ac;
    --photo-junior: #c9cdd3;
  }
  * { margin: 0; padding: 0; box-sizing: border-box; }
  html, body { width: 1200px; height: 916px; overflow: hidden; }
  body {
    background: var(--backdrop);
    font-family: "Open Sans", Arial, sans-serif;
    position: relative;
  }
  .letterhead {
    position: absolute;
    left: 268px; top: 28px;
    width: 665px; height: 860px;
    background: var(--paper);
    box-shadow: 0 6px 18px rgba(0,0,0,0.25);
  }
  .brand {
    position: absolute;
    right: 48px; top: 30px;
    text-align: right;
    line-height: 1;
  }
  .brand-name {
    font-size: 30px; font-weight: 800;
    color: var(--navy);
    letter-spacing: -0.5px;
  }
  .brand-domain {
    font-size: 11px; font-weight: 600;
    color: var(--muted);
    letter-spacing: 2px;
    margin-top: 3px;
  }
  .sidebar {
    position: absolute;
    left: 0; top: 110px;
    width: 150px; height: 750px;
    background: var(--navy);
  }
  .agent-photo {
    position: absolute;
    left: 12px;
    width: 126px; height: 82px;
    border: 4px solid var(--photo-frame);
  }
  .agent-photo.senior { top: 14px; background: linear-gradient(180deg, var(--photo-senior), #d8d4cf); }
  .agent-photo.junior { top: 106px; background: linear-gradient(180deg, var(--photo-junior), #e6e8eb); }
  .office-badge {
    position: absolute;
    left: 12px; bottom: 20px;
    width: 126px; height: 64px;
    background: var(--badge);
    border: 2px solid #ffffff;
    display: flex; align-items: center; justify-content: center; gap: 7px;
    padding: 0 8px;
  }
  .office-badge .mark {
    width: 10px; height: 10px; background: #ffffff; flex: none;
  }
  .office-badge .office-name {
    color: #ffffff;
    font-size: 13px; font-weight: 700;
    line-height: 1.15;
  }
  .letter-body {
    position: absolute;
    left: 186px; top: 180px;
    width: 440px;
    font-size: 8.5px;
    line-height: 1.45;
    color: var(--ink);
  }
  .letter-body p { margin-bottom: 9px; }
  .letter-body .salutation { margin-bottom: 6px; }
  .letter-body .closing { margin-top: 70px; }
  .site-footer {
    position: absolute;
    right: 40px; bottom: 36px;
    font-size: 16px;
    color: var(--muted);
  }
</style>
</head>
<body>
  <article class="letterhead">
    <header class="brand">
      <div class="brand-name">Prairieview</div>
      <div class="brand-domain">REALESTATE.COM</div>
    </header>

    <aside class="sidebar">
      <div class="agent-photo senior" role="img" aria-label="Head shot of senior agent"></div>
      <div class="agent-photo junior" role="img" aria-label="Head shot of junior agent"></div>
      <div class="office-badge">
        <span class="mark"></span>
        <span class="office-name">Marrowfield Hearth</span>
      </div>
    </aside>

    <section class="letter-body">
      <p class="salutation">Lorem Ipsum,</p>
      <p>Lorem ipsum dolor sit amet, consectetuer adipiscing elit. Nam cursus. Morbi ut mi. Nullam enim leo, egestas id, condimentum at, laoreet mattis, massa. Sed eleifend nonummy diam. Praesent mauris ante, elementum et, bibendum at, posuere sit amet, nibh. Duis tincidunt lectus quis dui viverra vestibulum. Suspendisse vulputate aliquam dui. Nulla elementum dui ut augue.</p>
      <p>Aliquam vehicula mi at mauris. Maecenas placerat, nisl at consequat rhoncus, sem nunc gravida justo, quis eleifend arcu velit quis lacus. Morbi magna magna, tincidunt a, mattis non, imperdiet vitae, tellus.</p>
      <p>Mauris nunc quam, venenatis nec, euismod sit amet, egestas placerat, est. Pellentesque habitant morbi tristique senectus et netus et malesuada fames ac turpis egestas. Cras id elit. Integer quis urna.</p>
      <p>Aliquam vehicula mi at mauris. Maecenas placerat, nisl at consequat rhoncus, sem nunc gravida justo, quis eleifend arcu velit quis lacus. Morbi magna magna, tincidunt a, mattis non, imperdiet vitae, tellus.</p>
      <p>Mauris nunc quam, venenatis nec, euismod sit amet, egestas placerat, est. Pellentesque habitant morbi tristique senectus et netus et malesuada fames ac turpis egestas. Cras id elit. Integer quis urna.</p>
      <p class="closing">Sincerly,</p>
    </section>

    <footer class="site-footer">www.prairieviewrealestate.com</footer>
  </article>
</body>
</html>
```